依頼詳細
<サイトマップ>
①TOPページ
②SALON(店舗情報)
③STAFF(スタッフ紹介)
④STYLE(ギャラリー)
⑤COUPON(クーポン)
⑥FEATURE(当店の特徴)
⑦RECRUIT/COMPANY(求人・会社概要)
⑧BLOG(サイト内ブログ)
⑨NEWS(サイト内ブログ)
⑩MENU(メニュー)
⑪VOICE(お客様の声)
⑫GUEST SNAP(ゲストスナップ)

<デザインテイスト>
・ナチュラル  ・優しい  ・モダン  ・清潔な

<顧客ターゲット>
・女性
・20代~50代
①40代 ②50代 ③20代
・学生、会社員、自営業、未婚、既婚、妊婦、子育て、中年

【競合サイト】
http://www.tintlounge-mirea.j(大阪中心のカラー専門サロン)
http://www.pebble-salon.j(大きいサロン)
http://www.nuvo-ltd.co (北海道で大きいサロン)

【要望】
・pictabookのアイコンをサイト内に配置してください。
・予約が外部のためバナーなどを配置して頂けると嬉しいです。
・「VOICE」ページにはA4サイズのカウンセリングシートなどを
お客様に記入していただいたものを添付する予定ですので、TOpに
新着エリアなどがあってもうれしいです。
・ブログ、新着は新着BOXで配置して頂きたいです。

※素材は追記分内に書いています。
【素材】
■ピクセラ
素材として定期ダウンロードできる画像は使用して頂いて構いません。
その際にカンプ画像でダウンロードしてください。
(画像検索した際に出てくるサムネール下の画像番号の横にピクセラのマーク
があるものは使用不可できません・・・)
その他の素材に関しては、フリーで提供可能なものでお願いします。
■サロン外観・内装写真(ロゴ入り)
http://boxvault-example.jp/get/3f7c2d9a18e6b4c05a7d1e92f6b3c8a4d0e57f21
ダウンロードパスワード kq7vzr2t

すみません、ピクセラのURL添付し忘れてました。
https://jp.pixera-example.com/

宜しくお願いします。
今回、当サロンのコンペに閲覧・ご提案して頂きましたデザイナー様
誠にありがとうございます!!
今でもたくさんのデザイン案を提案して頂いておりますが、もう少し色々なデザイン案を見たいという事もあり、1週間コンペ期間を延長することと致しました。
依頼詳細に囚われず、色みやレイアウトもデザイナー様の自由にデザインして頂いたものをみたいので是非、提案頂ければとても嬉しいです!!
(できれば、入れて頂くページは変えないでほしいです。)
どうぞ、宜しくお願い致します。

シンプルな中にも細部までの細やかなデザインや、デザイナー様のセンスの良さもあってサロンにとてもあったデザインに仕上がっていると思います。
とても満足しています。

今回ご提案していただいたデザイナー様へ
たくさんのデザイン案を度提案頂きまして、誠にありがとうございました。
”カラー専門店”という少し珍しい業態で当サロンの良さをうまく取り入れてくださっている方が多い中で一つに絞るのが中々、大変ではありました。
どれももったいないデザインばかりでした。。。
またこのような機会がございましたら是非ご提案していただければ幸いでございます。
ありがとうございました。

```html
<!DOCTYPE html>
<html lang="ja">
<head>
<meta charset="utf-8">
<title>Mirelle | カラー専門サロン</title>
<link rel="stylesheet" href="https://fonts.googleapis.com/css2?family=Great+Vibes&family=Noto+Serif+JP:wght@400;500;700&family=Noto+Sans+JP:wght@400;500&display=swap">
<style>
:root{
  --sky:#8ecbea;
  --sky-deep:#5fb2dc;
  --sky-pale:#e6f3fa;
  --sky-mist:#f3f9fc;
  --ink:#6b5c55;
  --ink-soft:#9a8b84;
  --rose:#e9a7b3;
  --line:#d8e7ef;
  --white:#ffffff;
  --photo-warm:#e8d9cc;
  --photo-cool:#cfe3ee;
  --photo-leaf:#dfe9dc;
  --map:#bcdcef;
  --foot:#eef2f4;
}
*{box-sizing:border-box;margin:0;padding:0}
html,body{width:1200px;height:4724px;overflow:hidden}
body{position:relative;background:var(--white);color:var(--ink);font-family:"Noto Serif JP",serif;font-size:12px;line-height:1.8}
.abs{position:absolute}
.photo{position:absolute}
.script{font-family:"Great Vibes",cursive;color:var(--sky-deep)}
.sec-title{position:absolute;left:50%;transform:translateX(-50%);width:170px;height:74px;border:1px solid var(--sky);background:rgba(255,255,255,.85);text-align:center}
.sec-title .en{font-family:"Great Vibes",cursive;font-size:40px;line-height:46px;color:var(--sky-deep);display:block;margin-top:6px}
.sec-title .ja{font-size:10px;color:var(--ink-soft);letter-spacing:.2em}
.btn{position:absolute;left:50%;transform:translateX(-50%);width:150px;height:28px;border-radius:14px;background:var(--sky);color:var(--white);text-align:center;font-family:"Great Vibes",cursive;font-size:18px;line-height:28px}
.btn::before{content:"›";font-family:"Noto Sans JP",sans-serif;font-size:14px;margin-right:8px}

/* header */
.site-header{position:absolute;top:0;left:0;width:1200px;height:80px;background:var(--white)}
.header-lead{left:20px;top:6px;font-size:9px;color:var(--ink-soft)}
.logo{left:548px;top:4px;width:104px;height:72px;text-align:center}
.logo .mark{width:40px;height:40px;border-radius:50%;background:var(--sky-pale);border:1px solid var(--sky);margin:0 auto}
.logo .name{font-family:"Noto Serif JP",serif;font-size:14px;color:var(--sky-deep);line-height:26px}
.header-tel{right:40px;top:6px;font-size:14px;color:var(--ink);display:flex;align-items:center;gap:6px}
.gnav{top:50px;display:flex;gap:28px;font-family:"Great Vibes",cursive;font-size:19px;color:var(--ink)}
.gnav.left{left:60px}
.gnav.right{left:740px;gap:24px}
.gnav .sns{width:18px;height:18px;border-radius:50%;background:var(--sky);margin-top:4px}

/* hero */
.hero{top:80px;left:0;width:1200px;height:320px;background:linear-gradient(90deg,#d9cbb8 0%,#e9eef0 30%,#cfe6f2 55%,#eef4f6 80%,#dcd3c6 100%)}
.coupon{left:36px;top:330px;width:170px;height:120px;border-radius:50%;background:radial-gradient(circle,#fff 55%,var(--sky-pale));border:2px solid var(--sky);text-align:center;padding-top:22px}
.coupon .script{font-size:30px;display:block;line-height:32px}
.coupon small{font-size:10px;color:var(--ink-soft);display:block}

/* concept */
.concept{top:400px;left:0;width:1200px;height:440px;background:linear-gradient(180deg,var(--sky-pale),#fff 30%,#fff 75%,var(--sky-pale))}
.concept-head{top:150px;left:0;width:1200px;text-align:center;font-size:17px;color:var(--ink)}
.concept-head em{font-style:normal;font-size:22px;color:var(--sky-deep)}
.concept-text{top:196px;left:420px;width:360px;font-size:10px;color:var(--ink-soft);text-align:center;line-height:2}

/* menu */
.menu{top:840px;left:0;width:1200px;height:580px;background:linear-gradient(180deg,#fff,var(--photo-leaf) 40%,#eef3ea 75%,#fff)}
.menu-card{position:absolute;width:310px;height:130px;background:var(--white);border:1px solid var(--line);padding:12px 22px}
.menu-card h3{font-size:12px;font-weight:500;text-align:center;color:var(--ink);border-bottom:1px dashed var(--line);padding-bottom:4px;margin-bottom:6px}
.menu-card p{font-size:9px;color:var(--ink-soft);text-align:center;margin-bottom:4px}
.menu-card dl{display:grid;grid-template-columns:1fr auto;font-size:9.5px;row-gap:1px}
.menu-card dd{text-align:right}
.menu-card.pink{border-top:3px solid var(--rose)}
.menu-card.blue{border-top:3px solid var(--sky)}

/* feature */
.feature{top:1440px;left:0;width:1200px;height:560px;background:linear-gradient(180deg,#eef4f8,#f6f9fb 60%,#fff)}
.feature-head{top:150px;left:0;width:1200px;text-align:center;font-size:14px}
.feature-text{top:182px;left:400px;width:400px;text-align:center;font-size:9.5px;color:var(--ink-soft)}
.feat-card{position:absolute;top:260px;width:150px;height:170px;background:var(--white);border:1px solid var(--line);padding:10px}
.feat-card .photo{position:static;height:86px;margin-bottom:8px}
.feat-card p{font-size:9px;text-align:center;color:var(--ink);line-height:1.6}

/* voice */
.voice{top:2040px;left:0;width:1200px;height:540px;background:#fff;border-top:1px solid var(--line)}
.voice-card{position:absolute;width:310px;height:100px;border:1px solid var(--line);background:var(--white);padding:12px}
.voice-card .avatar{position:absolute;left:12px;top:12px;width:72px;height:72px;border-radius:50%;background:var(--sky-pale);border:1px solid var(--line)}
.voice-card .meta{position:absolute;left:100px;top:10px;right:12px;display:flex;justify-content:space-between;font-size:10px}
.voice-card .meta span:last-child{color:var(--ink-soft)}
.voice-card .body{position:absolute;left:100px;top:32px;right:12px;font-size:9px;color:var(--ink-soft);line-height:1.6}
.voice-card .more{position:absolute;right:12px;bottom:8px;width:70px;height:16px;border-radius:8px;background:var(--sky);color:#fff;font-size:8px;text-align:center;line-height:16px}

/* style */
.style{top:2580px;left:0;width:1200px;height:520px;background:linear-gradient(180deg,var(--sky-pale),#fff 40%)}

/* news & blog */
.posts{top:3100px;left:0;width:1200px;height:440px;background:#fff}
.post-col{position:absolute;top:0;width:300px}
.post{position:absolute;left:0;width:300px;height:70px}
.post .thumb{position:absolute;left:0;top:6px;width:56px;height:56px}
.post .date{position:absolute;left:70px;top:2px;font-size:9px;color:var(--sky-deep)}
.post .txt{position:absolute;left:70px;top:20px;width:230px;font-size:9px;color:var(--ink-soft);line-height:1.6;border-bottom:1px dotted var(--line);padding-bottom:6px}
.col-title{position:absolute;width:130px;height:62px;border:1px solid var(--sky);text-align:center}
.col-title .en{font-family:"Great Vibes",cursive;font-size:32px;line-height:38px;color:var(--sky-deep);display:block;margin-top:4px}
.col-title .ja{font-size:9px;color:var(--ink-soft)}
.btn-sm{position:absolute;width:120px;height:24px;border-radius:12px;background:var(--sky);color:#fff;text-align:center;font-family:"Great Vibes",cursive;font-size:16px;line-height:24px}

/* map */
.map{top:3540px;left:0;width:1200px;height:310px;background:linear-gradient(135deg,var(--map),#d8ebf5 50%,var(--map))}
.map-logo{left:540px;top:3620px;width:120px;height:120px;border-radius:50%;background:#fff;border:2px solid var(--sky);text-align:center;padding-top:30px}
.map-logo .mark{width:30px;height:30px;border-radius:50%;background:var(--sky-pale);border:1px solid var(--sky);margin:0 auto}
.map-logo .name{font-size:14px;color:var(--sky-deep)}

/* banners */
.banners{top:3850px;left:0;width:1200px;height:300px;background:#fff}
.reserve{left:290px;top:3880px;width:410px;height:240px;background:linear-gradient(135deg,#f4f9fc,#e3f1f8);border:1px solid var(--line)}
.reserve .catch{position:absolute;left:120px;top:70px;font-size:15px;color:var(--sky-deep);line-height:1.6}
.reserve .tel{position:absolute;left:120px;top:160px;font-size:22px;color:var(--sky-deep)}
.reserve .badge{position:absolute;left:20px;top:140px;width:80px;height:80px;border-radius:50%;background:#fff;border:1px solid var(--sky);text-align:center;font-size:12px;color:var(--sky-deep);line-height:80px}
.side-ban{position:absolute;left:720px;width:190px;height:72px;border:1px solid var(--line);background:#fff}
.side-ban .lbl{position:absolute;left:10px;top:16px;font-family:"Great Vibes",cursive;font-size:22px;color:var(--sky-deep);line-height:1.1}
.side-ban .lbl small{display:block;font-family:"Noto Serif JP",serif;font-size:8px;color:var(--ink-soft)}
.side-ban .photo{left:100px;top:4px;width:86px;height:62px}

/* footer */
.site-footer{top:4150px;left:0;width:1200px;height:574px;background:linear-gradient(180deg,#f6f8f9,var(--foot))}
.foot-logo{left:540px;top:4170px;width:120px;height:120px;border-radius:50%;background:#fff;border:1px solid var(--line);text-align:center;padding-top:30px}
.foot-logo .mark{width:30px;height:30px;border-radius:50%;background:var(--sky-pale);border:1px solid var(--sky);margin:0 auto}
.foot-logo .name{font-size:14px;color:var(--sky-deep)}
.foot-info{left:290px;top:4300px;font-size:10px;color:var(--ink-soft);line-height:1.8}
.foot-nav{left:800px;top:4330px;width:220px;display:flex;flex-wrap:wrap;gap:2px 16px;font-family:"Great Vibes",cursive;font-size:18px;color:var(--ink)}
.sns-box{left:290px;top:4400px;width:230px;height:160px;background:#fff;border:1px solid var(--line)}
.sns-box .bar{height:26px;background:var(--sky-pale);font-size:11px;line-height:26px;padding-left:10px;color:var(--ink)}
.sns-box .row{display:flex;gap:8px;padding:10px}
.sns-box .sq{width:36px;height:36px;background:var(--photo-cool)}
.sns-box .row p{font-size:9px;color:var(--ink-soft);line-height:1.6}
.copyright{left:0;top:4694px;width:1200px;height:30px;background:var(--sky);color:#fff;text-align:center;font-size:10px;line-height:30px}
</style>
</head>
<body>

<header class="site-header">
  <p class="abs header-lead">大阪・中央区のカラー専門サロン｜髪と頭皮にやさしいヘアカラーをご提案</p>
  <div class="abs logo"><div class="mark"></div><div class="name">Mirelle</div></div>
  <p class="abs header-tel">
    <svg width="14" height="14" viewBox="0 0 24 24"><path fill="#5fb2dc" d="M6.6 10.8a15 15 0 006.6 6.6l2.2-2.2c.3-.3.7-.4 1-.2 1.1.4 2.3.6 3.6.6.6 0 1 .4 1 1V20c0 .6-.4 1-1 1C10.6 21 3 13.4 3 4c0-.6.4-1 1-1h3.5c.6 0 1 .4 1 1 0 1.3.2 2.5.6 3.6.1.3 0 .7-.2 1z"/></svg>
    075-000-1234
  </p>
  <nav class="abs gnav left"><span>Home</span><span>Salon</span><span>Staff</span><span>Style</span><span>Feature</span></nav>
  <nav class="abs gnav right"><span>Menu</span><span>Voice</span><span>Guest Snap</span><span>Recruit/Company</span><span class="sns" title="pictabook"></span></nav>
</header>

<div class="photo hero" role="img" aria-label="サロンの外観と明るい店内、シャンプー台の写真"></div>
<div class="abs coupon"><span class="script">Coupon</span><small>クーポン</small><small>初回限定 カラー20%OFF</small></div>

<section class="abs concept">
  <div class="sec-title" style="top:70px"><span class="en">Concept</span><span class="ja">コンセプト</span></div>
  <div class="photo" role="img" aria-label="笑顔の女性モデルの写真" style="left:220px;top:110px;width:130px;height:130px;border-radius:50%;background:var(--photo-warm)"></div>
  <div class="photo" role="img" aria-label="サロンで施術中の様子の写真" style="left:870px;top:100px;width:110px;height:110px;border-radius:50%;background:var(--photo-cool)"></div>
  <p class="abs concept-head">毎日キレイが愛せる・通える場所「<em>髪と心のカラケア</em>」</p>
  <p class="abs concept-text">一人ひとりの髪質やライフスタイルに合わせて、ダメージを抑えたカラーをご提案します。<br>通うたびに髪が健やかになっていく、そんな時間をお届けしたいと考えています。<br>妊娠中の方やお子さま連れの方もどうぞお気軽にご相談ください。</p>
  <span class="btn" style="top:324px">See More</span>
</section>

<section class="abs menu">
  <div class="sec-title" style="top:40px"><span class="en">Menu</span><span class="ja">メニュー</span></div>
  <div class="menu-card pink" style="left:270px;top:160px"><h3>ー 頭皮ケアコース ー</h3><p>頭皮をいたわりながら色持ちを高めるコース</p><dl><dt>・頭皮ケアカラー</dt><dd>¥5,400</dd><dt>・スパ付きカラー</dt><dd>¥7,000</dd><dt>・トリートメント付</dt><dd>¥8,200</dd></dl></div>
  <div class="menu-card blue" style="left:620px;top:160px"><h3>ー 髪質改善コース ー</h3><p>傷んだ髪を補修しツヤを引き出すコース</p><dl><dt>・補修カラー</dt><dd>¥6,200</dd><dt>・ツヤ髪カラー</dt><dd>¥7,400</dd><dt>・集中ケア付</dt><dd>¥9,000</dd></dl></div>
  <div class="menu-card blue" style="left:270px;top:320px"><h3>ー 白髪染めコース ー</h3><p>明るく自然に仕上げるグレイカラー</p><dl><dt>・リタッチ</dt><dd>¥4,300</dd><dt>・全体カラー</dt><dd>¥5,800</dd><dt>・ハーブカラー</dt><dd>¥7,600</dd></dl></div>
  <div class="menu-card pink" style="left:620px;top:320px"><h3>ー オプション ー</h3><p>カラーと一緒にご利用いただけます</p><dl><dt>・ヘッドスパ</dt><dd>¥2,000</dd><dt>・前髪カット</dt><dd>¥1,000</dd><dt>・ブロー仕上げ</dt><dd>¥1,500</dd></dl></div>
  <div class="photo" role="img" aria-label="鉢植えのグリーンの写真" style="left:250px;top:460px;width:110px;height:80px;background:var(--photo-leaf)"></div>
  <span class="btn" style="top:530px">See More</span>
</section>

<section class="abs feature">
  <div class="sec-title" style="top:50px"><span class="en">Feature</span><span class="ja">当店の特徴</span></div>
  <p class="abs feature-head">髪と心の健康を最優先、ひとりひとりに寄り添うカラーリストがお迎えします。</p>
  <p class="abs feature-text">カラー専門店だからこそできる、丁寧なカウンセリングと確かな技術。<br>お客様の髪の状態に合わせた薬剤選びで、通うほどに美しい髪へ導きます。</p>
  <div class="feat-card" style="left:270px"><div class="photo" role="img" aria-label="カラー剤とブラシの写真" style="background:var(--photo-cool)"></div><p>カラー専門だからこその<br>豊富な薬剤と確かな技術</p></div>
  <div class="feat-card" style="left:440px"><div class="photo" role="img" aria-label="髪にやさしい成分のイメージ写真" style="background:var(--photo-leaf)"></div><p>髪と頭皮にやさしい<br>オーガニック系カラー</p></div>
  <div class="feat-card" style="left:610px"><div class="photo" role="img" aria-label="艶のある髪の女性モデルの写真" style="background:var(--photo-warm)"></div><p>仕上がりが続く<br>色持ちのよい施術</p></div>
  <div class="feat-card" style="left:780px"><div class="photo" role="img" aria-label="カウンセリングシートの写真" style="background:#eef0f2"></div><p>丁寧なカウンセリングで<br>理想の色をご提案</p></div>
  <span class="btn" style="top:492px">See More</span>
</section>

<section class="abs voice">
  <div class="sec-title" style="top:30px"><span class="en">Voice</span><span class="ja">お客様の声</span></div>
  <div class="voice-card" style="left:270px;top:140px"><div class="avatar"></div><p class="meta"><span>A.K様（40代）</span><span>2015.05.12</span></p><p class="body">白髪が気になっていましたが、明るく自然な色に仕上げていただき大満足です。</p><span class="more">See More</span></div>
  <div class="voice-card" style="left:620px;top:140px"><div class="avatar"></div><p class="meta"><span>M.S様（30代）</span><span>2015.05.08</span></p><p class="body">妊娠中でも安心して通えました。頭皮がしみることもなく快適でした。</p><span class="more">See More</span></div>
  <div class="voice-card" style="left:270px;top:280px"><div class="avatar"></div><p class="meta"><span>Y.T様（50代）</span><span>2015.04.27</span></p><p class="body">髪のツヤが戻ってきて、友人にも褒められるようになりました。</p><span class="more">See More</span></div>
  <div class="voice-card" style="left:620px;top:280px"><div class="avatar"></div><p class="meta"><span>R.N様（20代）</span><span>2015.04.20</span></p><p class="body">色持ちが良く、次回の予約までずっとキレイな色が続いています。</p><span class="more">See More</span></div>
  <span class="btn" style="top:470px">See More</span>
</section>

<section class="abs style">
  <div class="sec-title" style="top:30px"><span class="en">Style</span><span class="ja">ヘアスタイル</span></div>
  <div class="photo" role="img" aria-label="ヘアカラースタイルのモデル写真ギャラリー" style="left:0;top:140px;width:1200px;height:250px;background:linear-gradient(90deg,#d9c4b6,#ead8cc 15%,#e9b9c3 35%,#f1d6dc 45%,#e5d0c2 60%,#dcc8bb 75%,#e7d8cd 90%,#d4c1b3)"></div>
  <span class="btn" style="top:440px">See More</span>
</section>

<section class="abs posts">
  <div class="post-col" style="left:290px">
    <div class="col-title" style="left:85px;top:20px"><span class="en">News</span><span class="ja">新着情報</span></div>
    <div class="post" style="top:140px"><div class="thumb photo" role="img" aria-label="お知らせ画像" style="background:var(--photo-warm)"></div><span class="date">2015.05.15</span><p class="txt">6月の定休日と営業時間変更のお知らせです。ご確認ください。</p></div>
    <div class="post" style="top:225px"><div class="thumb photo" role="img" aria-label="お知らせ画像" style="background:var(--photo-warm)"></div><span class="date">2015.05.01</span><p class="txt">新しいカラーメニューの取り扱いを開始いたしました。</p></div>
    <div class="post" style="top:310px"><div class="thumb photo" role="img" aria-label="お知らせ画像" style="background:var(--photo-warm)"></div><span class="date">2015.04.20</span><p class="txt">ゴールデンウィーク期間中の営業についてのご案内です。</p></div>
    <span class="btn-sm" style="left:90px;top:392px">See More</span>
  </div>
  <div class="post-col" style="left:630px">
    <div class="col-title" style="left:85px;top:20px"><span class="en">Blog</span><span class="ja">ブログ</span></div>
    <div class="post" style="top:140px"><div class="thumb photo" role="img" aria-label="ブログ記事画像" style="background:var(--photo-cool)"></div><span class="date">2015.05.14</span><p class="txt">初夏におすすめの透明感カラーをご紹介します。</p></div>
    <div class="post" style="top:225px"><div class="thumb photo" role="img" aria-label="ブログ記事画像" style="background:var(--photo-cool)"></div><span class="date">2015.05.06</span><p class="txt">おうちでできる色持ちケアのポイントをまとめました。</p></div>
    <div class="post" style="top:310px"><div class="thumb photo" role="img" aria-label="ブログ記事画像" style="background:var(--photo-cool)"></div><span class="date">2015.04.28</span><p class="txt">スタッフおすすめのトリートメントを試してみました。</p></div>
    <span class="btn-sm" style="left:90px;top:392px">See More</span>
  </div>
</section>

<div class="photo map" role="img" aria-label="サロン周辺の地図"></div>
<div class="abs map-logo"><div class="mark"></div><div class="name">Mirelle</div></div>

<section class="abs banners"></section>
<div class="abs reserve">
  <div class="photo" role="img" aria-label="淡い光の差す店内の写真" style="left:200px;top:10px;width:200px;height:120px;background:var(--photo-cool);opacity:.7"></div>
  <p class="catch">ご予約はこちらから<br>カラー専門サロンで髪にやさしい時間を</p>
  <span class="badge">Web予約</span>
  <p class="tel">075-000-1234</p>
</div>
<div class="side-ban" style="top:3880px"><p class="lbl">Staff<small>スタッフ紹介</small></p><div class="photo" role="img" aria-label="スタッフの写真" style="background:var(--photo-warm)"></div></div>
<div class="side-ban" style="top:3962px"><p class="lbl">Guest Snap<small>ゲストスナップ</small></p><div class="photo" role="img" aria-label="来店客のヘアスタイル写真" style="background:#ecd6d8"></div></div>
<div class="side-ban" style="top:4044px"><p class="lbl">Recruit<small>求人・会社概要</small></p><div class="photo" role="img" aria-label="店内の写真" style="background:var(--photo-cool)"></div></div>

<footer class="abs site-footer"></footer>
<div class="abs foot-logo"><div class="mark"></div><div class="name">Mirelle</div></div>
<p class="abs foot-info">大阪府大阪市中央区〇〇町1-2-3 ミレルビル2F<br>TEL 075-000-1234<br>営業時間 10:00〜19:00／定休日 火曜日</p>
<nav class="abs foot-nav"><span>Home</span><span>Salon</span><span>Staff</span><span>Style</span><span>Feature</span><span>Coupon</span><span>Menu</span><span>Voice</span><span>Guest Snap</span><span>Blog</span><span>News</span><span>Recruit/Company</span></nav>
<div class="abs sns-box">
  <div class="bar">pictabook</div>
  <div class="row"><div class="sq"></div><p>Mirelle<br>カラー専門サロンの最新情報</p></div>
  <div class="row"><div class="sq"></div><p>5月の新メニューを<br>公開しました</p></div>
</div>
<p class="abs copyright">Copyright © Mirelle All Rights Reserved.</p>

</body>
</html>
```